KAZ Freightworks #ALLKAZ Business Cards & Letterhead

I am looking to business cards designed for our organization. We are currently undergoing a small re-branding that is taking place. Our organization is called KAZ Freightworks and we are headquartered in Phoenix, AZ. We primarily provide transportation and logistics services to the Meridel Parcel Bureau who is our largest customer. I would like to see a design that incorporates name, title, contact info, website, and address (this will be different depending on the employee). I would also like to see some color on the business card using our logo colors or a variation. I would like our logo on the back of the business card with the website displayed. The final design should communicate that we are a next generation transportation operate that focuses on being driver-first, customer-centric, innovative, and sustainable.We would also like our #ALLKAZ catch phrase incorporated as well.
Updates

Decision maker traveling outside of the country until Monday, November 25th.

Target Market(s)

Transportation & Logistics

Industry/Entity Type

Trucking Company

Contact Information for Business Card

-First and Last Name
-Position Title
-Contact Phone
-Contact Email
-Physical Address

Font styles to use
Serif

Colors

Designer to choose colors to be used in the design.

Requirements
Must have
• -KAZ logo prominently displayed
• -#ALLKAZ catch phrase used
• -Some amount of color, design gradient, etc.
• -Logo on the back with website listed (https://www.kazfreightco.example)

```html
<!DOCTYPE html>
<html lang="en">
<head>
<meta charset="utf-8">
<title>KAZ Freightworks Stationery</title>
<link rel="stylesheet" href="https://fonts.googleapis.com/css2?family=Montserrat:wght@400;500;600;700;800&family=Tinos:wght@400;700&display=swap">
<style>
  :root {
    --green: #7dc242;
    --teal: #0d3f4a;
    --ink: #333a3d;
    --muted: #9aa3a6;
    --paper: #ffffff;
    --backdrop: #d9dadb;
  }
  * { margin: 0; padding: 0; box-sizing: border-box; }
  html, body { width: 1200px; height: 890px; overflow: hidden; }
  body { background: var(--backdrop); font-family: "Montserrat", sans-serif; color: var(--ink); position: relative; }

  .brand { display: flex; align-items: center; gap: 8px; font-family: "Montserrat", sans-serif; font-weight: 800; color: var(--teal); letter-spacing: 1px; }
  .brand-dot { border-radius: 50%; background: var(--green); flex: none; }

  .contact-block { font-family: "Tinos", serif; font-style: normal; color: var(--ink); }
  .contact-line { display: flex; align-items: center; gap: 6px; }
  .contact-line svg { width: 9px; height: 9px; fill: var(--green); flex: none; }
  .contact-gap { margin-top: 8px; }

  .tagline { font-family: "Tinos", serif; font-weight: 700; color: var(--green); letter-spacing: .5px; }

  /* Letterhead */
  .letterhead { position: absolute; left: 570px; top: 25px; width: 594px; height: 840px; background: var(--paper); box-shadow: 0 4px 14px rgba(0,0,0,.18); }
  .lh-contact { position: absolute; right: 48px; top: 40px; font-size: 11px; line-height: 1.35; }
  .lh-brand { position: absolute; left: 48px; top: 118px; font-size: 34px; }
  .lh-brand .brand-dot { width: 18px; height: 18px; }
  .lh-date { position: absolute; right: 48px; top: 200px; font-size: 8px; color: var(--muted); }
  .lh-recipient { position: absolute; left: 62px; top: 228px; font-size: 8px; }
  .recipient-label { font-size: 8px; }
  .recipient-name { font-weight: 700; font-size: 11px; color: var(--teal); margin-top: 2px; }
  .recipient-role { font-weight: 600; font-size: 8px; margin-bottom: 6px; }
  .recipient-row { display: flex; gap: 12px; line-height: 1.5; color: #666; font-size: 7.5px; }
  .recipient-row b { width: 8px; color: var(--ink); font-weight: 600; }
  .lh-body { position: absolute; left: 96px; right: 48px; top: 330px; font-size: 8px; line-height: 1.35; color: #4a4f52; text-align: justify; }
  .lh-body p { margin-bottom: 12px; }
  .lh-signature { position: absolute; left: 96px; top: 700px; }
  .sig-name { font-size: 11px; font-weight: 500; color: var(--ink); }
  .sig-role { font-size: 8px; color: var(--muted); }
  .lh-tagline { position: absolute; right: 48px; top: 722px; font-size: 12px; }
  .lh-band { position: absolute; left: 0; right: 128px; top: 762px; height: 14px; background: var(--teal); }
  .lh-accent { position: absolute; right: 0; top: 762px; width: 118px; height: 14px; background: var(--green); }
  .lh-footer { position: absolute; left: 0; right: 0; bottom: 0; height: 10px; background: var(--teal); }

  /* Cards */
  .card { position: absolute; width: 350px; height: 200px; border-radius: 16px; overflow: hidden; box-shadow: 0 4px 12px rgba(0,0,0,.2); }
  .card-back { left: 170px; top: 215px; background: linear-gradient(180deg, var(--green) 0%, #2f7a45 50%, var(--teal) 100%); }
  .card-map { position: absolute; inset: 14px 30px 30px 30px; border-radius: 8px; background: rgba(255,255,255,.06); }
  .card-back .brand { position: absolute; left: 50%; top: 78px; transform: translateX(-50%); font-size: 38px; color: #fff; }
  .card-back .brand-dot { width: 18px; height: 18px; background: #fff; }
  .card-url { position: absolute; left: 0; right: 0; bottom: 16px; text-align: center; font-size: 10px; color: #fff; letter-spacing: .5px; }

  .card-front { left: 170px; top: 445px; background: var(--paper); }
  .card-name { position: absolute; left: 22px; top: 28px; font-family: "Tinos", serif; font-weight: 700; font-size: 16px; color: var(--teal); }
  .card-role { position: absolute; left: 26px; top: 48px; font-family: "Tinos", serif; font-size: 10px; }
  .card-front .brand { position: absolute; right: 24px; top: 40px; font-size: 42px; }
  .card-front .brand-dot { width: 20px; height: 20px; }
  .card-contact { position: absolute; left: 26px; bottom: 20px; font-size: 10.5px; line-height: 1.35; }
  .card-tag { position: absolute; right: 26px; bottom: 22px; font-size: 13px; }
</style>
</head>
<body>

<article class="letterhead">
  <address class="lh-contact contact-block">
    <div>1480 Saguaro Way</div>
    <div>Phoenix AZ 85004</div>
    <div class="contact-line"><svg viewBox="0 0 10 10"><path d="M2 1l2 2-1 1.2c.6 1.2 1.6 2.2 2.8 2.8L7 6l2 2-1.4 1.4C4.5 9 1 5.5.6 2.4z"/></svg>(602) 555-0147</div>
    <div class="contact-line"><svg viewBox="0 0 10 10"><path d="M0 2h10v6H0zM0 2l5 3.5L10 2"/></svg>dana@kazfreightco.example</div>
    <div class="contact-line"><svg viewBox="0 0 10 10"><circle cx="5" cy="5" r="4.5"/></svg>www.kazfreightco.example</div>
  </address>

  <div class="lh-brand brand"><span class="brand-dot"></span>KAZ</div>
  <div class="lh-date">Friday, 01/01/2018</div>

  <div class="lh-recipient">
    <div class="recipient-label">To</div>
    <div class="recipient-name">Owen Tallis</div>
    <div class="recipient-role">Director</div>
    <div class="recipient-row"><b>A</b>220 Harbor Lane, Suite 12</div>
    <div class="recipient-row"><b>W</b>owen@tallisgroup.example, www.tallisgroup.example</div>
    <div class="recipient-row"><b>P</b>+1-480-555-0192</div>
  </div>

  <div class="lh-body">
    <p>Lorem ipsum dolor sit amet, consectetur adipiscing elit. Pellentesque facilisis sollicitudin ante. Pellentesque habitant morbi tristique senectus et netus et malesuada fames ac turpis egestas. Nunc feugiat tortor nunc, quis feugiat lectus mattis sit amet. Nunc urna velit, convallis scelerisque odio non, pulvinar tincidunt massa. Proin pulvinar lacus at ex auctor consequat. Maecenas eleifend tempus posuere. Aliquam non pretium metus. Mauris nibh velit, molestie et lorem quis, hendrerit lacinia nunc. Donec in dignissim augue. Curabitur vitae erat nisi. Vestibulum ante ipsum primis in faucibus orci luctus et ultrices posuere cubilia curae. Sed vel mi accumsan, luctus metus vel, congue ex.</p>
    <p>Curabitur non tristique tellus. Nam maximus fermentum metus sit amet luctus. Cras semper nunc id urna lacinia, in interdum quam mollis. Mauris sit amet eros vel lorem facilisis semper non ac nunc. Curabitur ornare suscipit lacus. Duis sit amet lectus vitae nulla consectetur ullamcorper vitae id urna. Sed dictum at lectus eget vehicula. Phasellus non lacinia nunc. Mauris ex tortor, ultricies luctus lectus egestas, gravida ornare elit. In tempor libero non ullamcorper sagittis. Nam a est at arcu porta auctor quis id tortor.</p>
    <p>Pellentesque habitant morbi tristique senectus et netus et malesuada fames ac turpis egestas. Nulla laoreet nec ex nec sagittis. Ut et vulputate magna. Nullam vehicula dapibus elit sagittis laoreet. Morbi dignissim ultricies libero at pulvinar. Sed leo tellus, ultricies nec erat sed, fermentum rhoncus odio. Pellentesque habitant morbi tristique senectus et netus et malesuada fames ac turpis egestas. Nullam egestas cursus dapibus. Integer non ante tincidunt, facilisis mauris sed, rutrum neque. Quisque purus risus, blandit quis iaculis vehicula, rutrum id felis.</p>
    <p>Etiam sed magna at ex vestibulum tincidunt in eget mi. Mauris ac elit et eros condimentum posuere sit amet ut augue. Suspendisse id auctor mi, a pretium ipsum. Suspendisse potenti. Duis in ex ut urna placerat viverra vel sed mi. Cras non congue augue. Integer ultricies non nibh quis ullamcorper. Phasellus sit amet lacus non velit maximus venenatis. Proin quam diam, sollicitudin non tincidunt at, elementum et neque. Aliquam eget congue nibh, laoreet viverra purus. Donec rhoncus nibh sit amet blandit tincidunt. Suspendisse eu turpis vel sapien tincidunt faucibus.</p>
  </div>

  <div class="lh-signature">
    <div class="sig-name">Priya Coleman</div>
    <div class="sig-role">Managing Director</div>
  </div>

  <div class="lh-tagline tagline">#ALLKAZ</div>

  <div class="lh-band"></div>
  <div class="lh-accent"></div>
  <div class="lh-footer"></div>
</article>

<section class="card card-back">
  <div class="card-map" role="img" aria-label="Faint outline map of the United States behind the name"></div>
  <div class="brand"><span class="brand-dot"></span>KAZ</div>
  <div class="card-url">www.kazfreightco.example</div>
</section>

<section class="card card-front">
  <div class="card-name">Dana Reyes</div>
  <div class="card-role">Owner</div>
  <div class="brand"><span class="brand-dot"></span>KAZ</div>
  <address class="card-contact contact-block">
    <div>1480 Saguaro Way</div>
    <div>Phoenix AZ 85004</div>
    <div class="contact-line contact-gap"><svg viewBox="0 0 10 10"><path d="M2 1l2 2-1 1.2c.6 1.2 1.6 2.2 2.8 2.8L7 6l2 2-1.4 1.4C4.5 9 1 5.5.6 2.4z"/></svg>(602) 555-0147</div>
    <div class="contact-line"><svg viewBox="0 0 10 10"><path d="M0 2h10v6H0zM0 2l5 3.5L10 2"/></svg>dana@kazfreightco.example</div>
    <div class="contact-line"><svg viewBox="0 0 10 10"><circle cx="5" cy="5" r="4.5"/></svg>www.kazfreightco.example</div>
  </address>
  <div class="card-tag tagline">#ALLKAZ</div>
</section>

</body>
</html>
```